Fernhollow Estates Cards and Letterhead
EPS and PNG formatted logo files have been uploaded
Please feel free to post ideas for letterhead / stationary as well. Thanks.
SiteAdmin - I haven't yet received my logo files. If there is somewhere I can download them from please let me know. Thanks.
Attention Project Holder!!
Please be advised to upload your logo file in AI, EPS or PNG format so that the designers can incorporate your logo in this designs.
QT/PWF/HR Team
If you have the ability to create a couple of PowerPoint master slides based on the look and feel of the logo I'd be willing to pay extra for those. Thx.

```html
<!DOCTYPE html>
<html lang="en">
<head>
<meta charset="utf-8">
<title>Fernhollow Estates Business Card</title>
<link href="https://fonts.googleapis.com/css2?family=Arimo:wght@400;700&display=swap" rel="stylesheet">
<style>
  :root {
    --backdrop: #3b3b3d;
    --card-white: #ffffff;
    --navy: #1f3773;
    --green: #3fa535;
    --text-light: #ffffff;
    --text-soft: #d9def0;
  }
  * { margin: 0; padding: 0; box-sizing: border-box; }
  html, body {
    width: 1200px; height: 780px; overflow: hidden;
    background: var(--backdrop);
    font-family: "Arimo", Arial, sans-serif;
  }
  .canvas {
    width: 1200px; height: 780px;
    display: flex; align-items: center; justify-content: center;
  }
  .business-card {
    position: relative;
    width: 1050px; height: 600px;
    background: var(--card-white);
    border-radius: 34px;
    overflow: hidden;
  }
  .card-waves { position: absolute; inset: 0; width: 100%; height: 100%; }
  .wave-green { fill: var(--green); }
  .wave-navy { fill: var(--navy); }

  .brand {
    position: absolute; left: 160px; top: 130px;
    display: flex; align-items: center; gap: 18px;
  }
  .brand-mark {
    width: 54px; height: 54px; background: var(--navy);
  }
  .brand-name {
    color: var(--navy);
    font-weight: 700;
    font-size: 46px;
    letter-spacing: 1px;
    line-height: 1;
    text-transform: uppercase;
  }
  .brand-name .brand-suffix { display: block; text-align: right; margin-top: 4px; }

  .holder {
    position: absolute; left: 120px; top: 410px; width: 300px;
    text-align: right; color: var(--text-light);
  }
  .holder-name { font-size: 28px; font-weight: 700; margin-bottom: 14px; }
  .holder-title, .holder-address { font-size: 18px; color: var(--text-soft); line-height: 1.5; }
  .holder-title { margin-bottom: 10px; }

  .contacts {
    position: absolute; left: 470px; top: 380px;
    list-style: none; color: var(--text-soft); font-size: 19px;
  }
  .contacts li { display: flex; align-items: center; gap: 14px; height: 34px; }
  .contacts svg { width: 22px; height: 22px; fill: var(--text-light); flex: none; }
  .contacts .contact-email { font-size: 17px; }
</style>
</head>
<body>
<main class="canvas">
  <article class="business-card">
    <svg class="card-waves" viewBox="0 0 1050 600" preserveAspectRatio="none" aria-hidden="true">
      <path class="wave-green" d="M0,338 C260,395 620,318 1050,215 L1050,600 L0,600 Z"/>
      <path class="wave-navy" d="M0,362 C290,420 650,345 1050,250 L1050,600 L0,600 Z"/>
    </svg>

    <header class="brand">
      <span class="brand-mark"></span>
      <h1 class="brand-name">Fernhollow Estates<span class="brand-suffix">LLC</span></h1>
    </header>

    <section class="holder">
      <p class="holder-name">Rowan Villaine</p>
      <p class="holder-title">Your Job Title</p>
      <p class="holder-address">Suite 102 Street name,<br>State, Zip 2034,Country</p>
    </section>

    <ul class="contacts">
      <li>
        <svg viewBox="0 0 24 24"><path d="M6.6 10.8c1.4 2.8 3.8 5.1 6.6 6.6l2.2-2.2c.3-.3.7-.4 1-.2 1.1.4 2.3.6 3.6.6.6 0 1 .4 1 1V20c0 .6-.4 1-1 1C10.6 21 3 13.4 3 4c0-.6.4-1 1-1h3.5c.6 0 1 .4 1 1 0 1.3.2 2.5.6 3.6.1.3 0 .7-.2 1z"/></svg>
        <span>555 014 2281</span>
      </li>
      <li>
        <svg viewBox="0 0 24 24"><path d="M7 2h10c1.1 0 2 .9 2 2v16c0 1.1-.9 2-2 2H7c-1.1 0-2-.9-2-2V4c0-1.1.9-2 2-2zm0 3v12h10V5zm5 13.5a1.2 1.2 0 100 2.4 1.2 1.2 0 000-2.4z"/></svg>
        <span>555 014 2282</span>
      </li>
      <li>
        <svg viewBox="0 0 24 24"><path d="M7 3h10v5H7zM4 9h16c1.1 0 2 .9 2 2v6h-4v4H6v-4H2v-6c0-1.1.9-2 2-2zm4 7v3h8v-3z"/></svg>
        <span>555 014 2283</span>
      </li>
      <li>
        <svg viewBox="0 0 24 24"><path d="M3 5h18c.6 0 1 .4 1 1v12c0 .6-.4 1-1 1H3c-.6 0-1-.4-1-1V6c0-.6.4-1 1-1zm1 2.3V17h16V7.3l-8 5.2z M4.8 7L12 11.7 19.2 7z"/></svg>
        <span class="contact-email">rowan.villaine@fernhollowestatesllc.com</span>
      </li>
    </ul>
  </article>
</main>
</body>
</html>
```